Use responsive design to make this page look and behave awesome in any size

YOU CAN SUBMIT PSD, HOWEVER, THE WINNER MUST SUBMIT PROVIDE A SINGLE CODED PAGE PER THE LINK AND INSTRUCTIONS AT THE BOTTOM OF THIS BRIEF. While developing an internal website, we realized we are not super great at making things look awesome and responsive for phone/tablet/desktop. Thats where you come in. We want you to take this code, Fork it, and then make it look awesome and work great on any size device.

Task at hand:

This page is a simple dashboard showing how a number of stores stack up against each other and against a corporate goal.

Top: Goal title, and where the logged in person's store stands in the ranking.
Green means you are in compliance
Red means you are not in compliance

Middle: Description of goal. Words to describe what the corporate goal is, and a target number.

Bottom: Here we just want to show the top 10 and bottom 5 out of 100+ stores. if your in the top ten, you are highlighted. If your in the bottom 5, you will be highlighted there too. If you are in the middle, we would put the your store info between the top and bottom... indicating your in the middle.
Green means you they are in compliance
Red means they are not in compliance

Your Mission is not only to make this look fantastic and responsive, but to have usable code in there.

You don't need to do any logic. All we care about is look and feel and responsive behavior on different size browsers.

The winner obviously gets the prize, and hopefully can become a solid resource to do more of this type of thing for us in the future.

Instructions:
Go to this link: https://codequill.example/edit/tvx-leaderpanel-widget
Click on the blue Fork button. This will give you a new URL that you can paste back into the contest to review results for us to see your work.
Uploading pictures is not necessary as the responsive code is what is important here.

Good luck!

Number of Pages Required

1 page

Requirements
Must have
• The page must be responsive and look very professional AND game like.
Should not have
• plugins. just native code

```html
<!DOCTYPE html>
<html lang="en">
<head>
<meta charset="utf-8">
<title>Lead Measures</title>
<link href="https://fonts.googleapis.com/css2?family=Poppins:wght@400;500;700&display=swap" rel="stylesheet">
<style>
:root{
  --blue:#1d9bf0;
  --blue-edge:#1a8fe3;
  --panel:#f4f4f4;
  --line:#dcdcdc;
  --text:#333;
  --green:#27a04a;
  --green-dark:#1d6b34;
  --page:#ffffff;
}
*{box-sizing:border-box;margin:0;padding:0}
html,body{width:1200px;height:4467px;overflow:hidden;background:var(--page);font-family:'Poppins',sans-serif;color:var(--text)}
.page-title{position:absolute;top:70px;left:0;width:1200px;text-align:center;font-weight:700;font-size:52px;letter-spacing:1px;color:var(--blue)}
.measure-card{position:absolute;left:71px;width:1061px;height:975px;background:#fff;border-left:5px solid var(--blue-edge);box-shadow:0 2px 14px rgba(0,0,0,.14);padding:48px 45px 0 43px}
.measure-panel{background:var(--panel);border:1px solid var(--line);height:873px}
.measure-head{height:150px;display:flex;align-items:center;justify-content:center;gap:30px}
.measure-name{font-size:52px;font-weight:400;color:#222}
.score-ring{position:relative;width:108px;height:108px}
.score-ring svg{position:absolute;inset:0}
.score-value{position:absolute;inset:0;display:flex;align-items:center;justify-content:center;font-size:28px;font-weight:500;color:var(--green-dark)}
.score-value small{font-size:15px;margin-top:8px}
.goal-band{height:78px;background:var(--blue);color:#fff;display:flex;align-items:center;font-size:20px}
.goal-text{width:790px;padding-left:40px}
.goal-target{padding-left:0}
.rank-row{height:52px;display:flex;align-items:center;background:#fff;border-bottom:1px solid var(--line);font-size:15px}
.rank-row span{height:100%;display:flex;align-items:center}
.rank-pos{width:232px;padding-left:50px;border-right:1px solid var(--line)}
.rank-store{width:447px;justify-content:center;border-right:1px solid var(--line)}
.rank-value{padding-left:155px}
.rank-gap{height:21px;background:#fff;border-bottom:1px solid var(--line)}
.rank-row.is-you{position:relative;margin:0 -8px;padding:0 8px;box-shadow:0 2px 10px rgba(0,0,0,.22);z-index:1}
</style>
</head>
<body>
<h1 class="page-title">LEAD MEASURES</h1>

<section class="measure-card" style="top:188px">
  <div class="measure-panel">
    <div class="measure-head">
      <h2 class="measure-name">Team</h2>
      <div class="score-ring">
        <svg viewBox="0 0 108 108"><circle cx="54" cy="54" r="48" fill="#fff" stroke="var(--green)" stroke-width="8"/></svg>
        <div class="score-value">92.1<small>%</small></div>
      </div>
    </div>
    <div class="goal-band"><span class="goal-text">Use Slow Stock wherever possible</span><span class="goal-target">80%</span></div>
    <div class="rank-row"><span class="rank-pos">1</span><span class="rank-store">(1) yjcQbtCyOu</span><span class="rank-value">1%</span></div>
    <div class="rank-row"><span class="rank-pos">2</span><span class="rank-store">(1) crsmichxwS</span><span class="rank-value">1%</span></div>
    <div class="rank-row"><span class="rank-pos">3</span><span class="rank-store">(2) wnLJojLRSf</span><span class="rank-value">2%</span></div>
    <div class="rank-row"><span class="rank-pos">4</span><span class="rank-store">(2) swEbjeRrpI</span><span class="rank-value">2%</span></div>
    <div class="rank-row"><span class="rank-pos">5</span><span class="rank-store">(4) aUasMPhcOA</span><span class="rank-value">4%</span></div>
    <div class="rank-row"><span class="rank-pos">6</span><span class="rank-store">(5) vYuFdHZExl</span><span class="rank-value">5%</span></div>
    <div class="rank-row"><span class="rank-pos">7</span><span class="rank-store">(5) jvBnNdGkel</span><span class="rank-value">5%</span></div>
    <div class="rank-row"><span class="rank-pos">8</span><span class="rank-store">(6) CuW8vexCs</span><span class="rank-value">6%</span></div>
    <div class="rank-row"><span class="rank-pos">9</span><span class="rank-store">(7) XQFCUbSoko</span><span class="rank-value">7%</span></div>
    <div class="rank-row"><span class="rank-pos">10</span><span class="rank-store">(7) GucpFDVVJP</span><span class="rank-value">7%</span></div>
    <div class="rank-gap"></div>
    <div class="rank-row"><span class="rank-pos">96</span><span class="rank-store">(94) VaDGNkvwal</span><span class="rank-value">94%</span></div>
    <div class="rank-row"><span class="rank-pos">97</span><span class="rank-store">(94) BljPTBGSh</span><span class="rank-value">94%</span></div>
  </div>
</section>

<section class="measure-card" style="top:1245px">
  <div class="measure-panel">
    <div class="measure-head">
      <h2 class="measure-name">Slow</h2>
      <div class="score-ring">
        <svg viewBox="0 0 108 108"><circle cx="54" cy="54" r="48" fill="#fff" stroke="var(--green-dark)" stroke-width="8"/></svg>
        <div class="score-value">0<small>%</small></div>
      </div>
    </div>
    <div class="goal-band"><span class="goal-text">Less than 0% of inventory slower than 100 days</span><span class="goal-target">&lt; 1%</span></div>
    <div class="rank-row"><span class="rank-pos">1</span><span class="rank-store">(89) NZBGVumnc</span><span class="rank-value">0%</span></div>
    <div class="rank-row"><span class="rank-pos">2</span><span class="rank-store">(80) GaccDeNKUO</span><span class="rank-value">0%</span></div>
    <div class="rank-row"><span class="rank-pos">3</span><span class="rank-store">(55) aiPpNcqcDh</span><span class="rank-value">0%</span></div>
    <div class="rank-row"><span class="rank-pos">4</span><span class="rank-store">(97) YqyVfKThl</span><span class="rank-value">0%</span></div>
    <div class="rank-row"><span class="rank-pos">5</span><span class="rank-store">(67) PvQdqyeaHr</span><span class="rank-value">0%</span></div>
    <div class="rank-row is-you"><span class="rank-pos">6</span><span class="rank-store">(00) Your Store</span><span class="rank-value">2%</span></div>
    <div class="rank-row"><span class="rank-pos">7</span><span class="rank-store">(40) jyMYYVbl</span><span class="rank-value">2%</span></div>
    <div class="rank-row"><span class="rank-pos">8</span><span class="rank-store">(11) QSESmpDJqw</span><span class="rank-value">2%</span></div>
    <div class="rank-row"><span class="rank-pos">9</span><span class="rank-store">(71) nBoXFjUWv</span><span class="rank-value">2%</span></div>
    <div class="rank-row"><span class="rank-pos">10</span><span class="rank-store">(51) EhKkkveKpb</span><span class="rank-value">2%</span></div>
    <div class="rank-gap"></div>
    <div class="rank-row"><span class="rank-pos">96</span><span class="rank-store">(90) VZgTuWgJTU</span><span class="rank-value">8%</span></div>
    <div class="rank-row"><span class="rank-pos">97</span><span class="rank-store">(67) nRGVsKcZhP</span><span class="rank-value">9%</span></div>
  </div>
</section>

<section class="measure-card" style="top:2340px">
  <div class="measure-panel">
    <div class="measure-head">
      <h2 class="measure-name">Turns</h2>
      <div class="score-ring">
        <svg viewBox="0 0 108 108"><circle cx="54" cy="54" r="48" fill="#fff" stroke="var(--green-dark)" stroke-width="8"/></svg>
        <div class="score-value">2.2</div>
      </div>
    </div>
    <div class="goal-band"><span class="goal-text">Turn inventory 6 or more times a year</span><span class="goal-target">&gt; 6</span></div>
    <div class="rank-row"><span class="rank-pos">1</span><span class="rank-store">(8) VZaEOSVkeF</span><span class="rank-value">0.2</span></div>
    <div class="rank-row"><span class="rank-pos">2</span><span class="rank-store">(3) PcVKNpUNmj</span><span class="rank-value">0.2</span></div>
    <div class="rank-row"><span class="rank-pos">3</span><span class="rank-store">(4) RRyRZsTm</span><span class="rank-value">0.4</span></div>
    <div class="rank-row"><span class="rank-pos">4</span><span class="rank-store">((9) epINQFfE</span><span class="rank-value">0.6</span></div>
    <div class="rank-row"><span class="rank-pos">5</span><span class="rank-store">(3) FbFOdjSpF</span><span class="rank-value">0.7</span></div>
    <div class="rank-row is-you"><span class="rank-pos">6</span><span class="rank-store">(7) RdzbKcVqEC</span><span class="rank-value">0.8</span></div>
    <div class="rank-row"><span class="rank-pos">7</span><span class="rank-store">(1) DItXKIIkTx</span><span class="rank-value">0.8</span></div>
    <div class="rank-row"><span class="rank-pos">8</span><span class="rank-store">(1) jxWbwOKyVa</span><span class="rank-value">0.8</span></div>
    <div class="rank-row"><span class="rank-pos">9</span><span class="rank-store">(4) UyznfRMiU</span><span class="rank-value">0.8</span></div>
    <div class="rank-row"><span class="rank-pos">10</span><span class="rank-store">(4) KVIgJQBgAC</span><span class="rank-value">1</span></div>
    <div class="rank-gap"></div>
    <div class="rank-row"><span class="rank-pos">96</span><span class="rank-store">(5) gBwGhPgZNF</span><span class="rank-value">9.7</span></div>
    <div class="rank-row"><span class="rank-pos">97</span><span class="rank-store">(8) gGhhZfICH</span><span class="rank-value">9.7</span></div>
  </div>
</section>

<section class="measure-card" style="top:3371px">
  <div class="measure-panel">
    <div class="measure-head">
      <h2 class="measure-name">Values</h2>
      <div class="score-ring">
        <svg viewBox="0 0 108 108"><circle cx="54" cy="54" r="48" fill="#fff" stroke="var(--green-dark)" stroke-width="8"/></svg>
        <div class="score-value">1.9</div>
      </div>
    </div>
    <div class="goal-band"><span class="goal-text">Inventory Value to be around 1.25 x you last months INVENTORY sales</span><span class="goal-target">1.25</span></div>
    <div class="rank-row"><span class="rank-pos">1</span><span class="rank-store">(8) VZaEOSVkeF</span><span class="rank-value">0.2</span></div>
    <div class="rank-row"><span class="rank-pos">2</span><span class="rank-store">3) PcVKNpUNmj</span><span class="rank-value">0.2</span></div>
    <div class="rank-row"><span class="rank-pos">3</span><span class="rank-store">(4) RRyRZsTm</span><span class="rank-value">0.4</span></div>
    <div class="rank-row"><span class="rank-pos">4</span><span class="rank-store">((9) epINQFfE</span><span class="rank-value">0.6</span></div>
    <div class="rank-row"><span class="rank-pos">5</span><span class="rank-store">(3) FbFOdjSpF</span><span class="rank-value">0.7</span></div>
    <div class="rank-row is-you"><span class="rank-pos">6</span><span class="rank-store">(7) RdzbKcVqEC</span><span class="rank-value">0.8</span></div>
    <div class="rank-row"><span class="rank-pos">7</span><span class="rank-store">(1) DItXKIIkTx</span><span class="rank-value">0.8</span></div>
    <div class="rank-row"><span class="rank-pos">8</span><span class="rank-store">(1) jxWbwOKyVa</span><span class="rank-value">0.8</span></div>
    <div class="rank-row"><span class="rank-pos">9</span><span class="rank-store">(4) UyznfRMiU</span><span class="rank-value">0.8</span></div>
    <div class="rank-row"><span class="rank-pos">10</span><span class="rank-store">(4) KVIgJQBgAC</span><span class="rank-value">1</span></div>
    <div class="rank-gap"></div>
    <div class="rank-row"><span class="rank-pos">96</span><span class="rank-store">(5) gBwGhPgZNF</span><span class="rank-value">9.7</span></div>
    <div class="rank-row"><span class="rank-pos">97</span><span class="rank-store">(8) gGhhZfICH</span><span class="rank-value">9.7</span></div>
  </div>
</section>
</body>
</html>
```